Label for Refill packaging eco-conscious beauty brand

We need a label for our refill pouch. Velvet Harbor is an unscented conditioner formulated using the finest healthy & pure ingredients, free of chemicals and harmful toxins. As a minimalist beauty brand we are proud to be certified with TQB, Norvamark and Silver Kestrel.

We already have the pouches and an exciting label for our regular bottles.
We choose a kraft brown packing for the refill pouch and would like something minimalist but elegant for the label.

```html
<!DOCTYPE html>
<html lang="en">
<head>
<meta charset="utf-8">
<title>Velvet Harbor – Refill Pouch Label</title>
<link rel="stylesheet" href="https://fonts.googleapis.com/css2?family=Italiana&family=Montserrat:wght@400;500&display=swap">
<style>
  :root {
    --backdrop: #c5dea2;
    --label-light: #ecd3c8;
    --label-dark: #d3b3a6;
    --band-mauve: #8a7077;
    --band-stripe: #7d656c;
    --gold-light: #f0d27a;
    --gold: #d4a935;
    --gold-deep: #b88a22;
    --ink: #76606a;
    --ink-soft: #a58d91;
    --badge-green: #3f9a55;
    --badge-teal: #4ea6b0;
    --badge-leaf: #6aa06a;
  }
  * { margin: 0; padding: 0; box-sizing: border-box; }
  html, body {
    width: 1200px;
    height: 1100px;
    overflow: hidden;
    background: var(--backdrop);
  }
  .canvas {
    position: relative;
    width: 1200px;
    height: 1100px;
  }
  .label {
    position: absolute;
    left: 330px;
    top: 150px;
    width: 540px;
    height: 800px;
    background: radial-gradient(ellipse at 50% 40%, var(--label-light) 0%, var(--label-dark) 100%);
    border-radius: 16px;
    overflow: hidden;
    text-align: center;
  }
  .leaf-band {
    position: absolute;
    left: 0; top: 0;
    width: 100%;
    height: 177px;
    background:
      linear-gradient(115deg, rgba(230,195,90,0.35) 0%, rgba(138,112,119,0) 35%, rgba(230,195,90,0.3) 60%, rgba(138,112,119,0) 85%),
      var(--band-mauve);
  }
  .leaf-band-stripe {
    position: absolute;
    left: 0; top: 177px;
    width: 100%;
    height: 11px;
    background: var(--band-stripe);
  }
  .brand {
    position: absolute;
    left: 0; right: 0;
    top: 300px;
    display: flex;
    flex-direction: column;
    align-items: center;
    gap: 18px;
  }
  .brand-square {
    width: 44px;
    height: 44px;
    background: linear-gradient(135deg, var(--gold-light), var(--gold) 50%, var(--gold-deep));
  }
  .brand-name {
    font-family: "Montserrat", sans-serif;
    font-weight: 500;
    font-size: 24px;
    line-height: 1.15;
    letter-spacing: 1px;
    color: var(--ink);
  }
  .product-name {
    position: absolute;
    left: 0; right: 0;
    top: 488px;
    font-family: "Italiana", serif;
    font-size: 48px;
    color: var(--ink);
    letter-spacing: 0.5px;
  }
  .gold-rule {
    position: absolute;
    left: 217px;
    top: 579px;
    width: 106px;
    height: 20px;
    background: linear-gradient(90deg, var(--gold-deep), var(--gold-light) 45%, var(--gold) 70%, var(--gold-deep));
  }
  .descriptor {
    position: absolute;
    left: 0; right: 0;
    top: 636px;
    font-family: "Montserrat", sans-serif;
    font-size: 13px;
    letter-spacing: 1.2px;
    line-height: 20px;
  }
  .descriptor-en { color: var(--ink); font-weight: 500; }
  .descriptor-fr { color: var(--ink-soft); font-weight: 400; }
  .certifications {
    position: absolute;
    left: 0; right: 0;
    top: 704px;
    display: flex;
    justify-content: center;
    gap: 30px;
  }
  .certifications svg { display: block; }
  .volume {
    position: absolute;
    left: 0; right: 0;
    top: 757px;
    font-family: "Montserrat", sans-serif;
    font-size: 9.5px;
    font-weight: 500;
    letter-spacing: 0.8px;
    color: var(--ink);
  }
</style>
</head>
<body>
<div class="canvas">
  <div class="label">
    <div class="leaf-band" role="img" aria-label="Gold leaf-vein pattern on mauve band"></div>
    <div class="leaf-band-stripe"></div>

    <div class="brand">
      <div class="brand-square"></div>
      <div class="brand-name">KLAAR<br>Maren</div>
    </div>

    <h1 class="product-name">Velvet Harbor</h1>

    <div class="gold-rule"></div>

    <div class="descriptor">
      <p class="descriptor-en">UNSCENTED HAIR CONDITIONER</p>
      <p class="descriptor-fr">APRÈS-SHAMPOING NON PARFUMÉ</p>
    </div>

    <div class="certifications">
      <svg width="24" height="24" viewBox="0 0 24 24" aria-label="TQB certification">
        <circle cx="12" cy="12" r="11" fill="var(--badge-green)"/>
      </svg>
      <svg width="26" height="26" viewBox="0 0 26 26" aria-label="Norvamark certification">
        <circle cx="13" cy="13" r="12" fill="var(--badge-teal)"/>
      </svg>
      <svg width="26" height="26" viewBox="0 0 26 26" aria-label="Silver Kestrel certification">
        <circle cx="13" cy="13" r="11" fill="none" stroke="var(--badge-leaf)" stroke-width="2"/>
      </svg>
    </div>

    <p class="volume">238 ml ℮ 8 Fl. Oz.</p>
  </div>
</div>
</body>
</html>
```